WooCommerce Web Design for SEO Agency

Looking for a clean and fast WooCommerce design

Selling 5 different products each with maybe 3-4 variants

Need imagery - featured images, basic logo etc

I will supply all content and most is ready to go (or can be in a few days)

You will need to design and build the site including some basic WooCommerce configuration - PayPal, checkout forms etc

Target Market(s)

SEO, Internet marketers

Coding

Coded - Design and coding required

Number of Pages Required

3 page

Font styles to use
Sans Serif

Requirements
Must have
• WooCommerce and WP integration

```html
<!DOCTYPE html>
<html lang="en">
<head>
<meta charset="utf-8">
<title>RankLift – SEO Link Building</title>
<link href="https://fonts.googleapis.com/css2?family=Open+Sans:wght@300;400;600;700&display=swap" rel="stylesheet">
<style>
:root{
  --blue:#1f6db5;
  --blue-dark:#1b4f86;
  --navy:#1d3d63;
  --footer:#17365a;
  --grey-bg:#f2f4f6;
  --grey-head:#8a8a8a;
  --grey-btn:#7d7d7d;
  --text:#555;
  --muted:#777;
  --line:#d9d9d9;
  --white:#fff;
  --green:#4caf50;
}
*{box-sizing:border-box;margin:0;padding:0}
html,body{width:1200px;height:3092px;overflow:hidden}
body{font-family:"Open Sans",sans-serif;color:var(--text);background:var(--white);position:relative}
.abs{position:absolute}
.topbar{left:0;top:0;width:1200px;height:32px;background:var(--blue);color:#fff;font-size:14px;display:flex;justify-content:flex-end;align-items:center;gap:22px;padding-right:92px}
.topbar span{display:flex;align-items:center;gap:6px}
.nav{left:0;top:32px;width:1200px;height:58px;background:#fff;display:flex;align-items:center;padding:0 92px;justify-content:space-between}
.brand{display:flex;align-items:center;gap:8px;font-size:31px;font-weight:600;color:var(--blue)}
.brand i{width:30px;height:30px;border-radius:50%;background:var(--blue);display:block}
.menu{display:flex;gap:50px;font-size:15px;color:#666;align-items:center}
.menu .active{color:var(--blue)}
.hero{left:0;top:90px;width:1200px;height:400px;background:linear-gradient(100deg,#9bb8d3 0%,#6f98c0 45%,#2f67a3 100%)}
.hero-copy{left:89px;top:222px;color:#fff}
.hero-copy h1{font-size:34px;font-weight:600;text-shadow:0 2px 4px rgba(0,0,0,.3)}
.hero-copy p{font-size:15px;font-weight:300;margin-top:10px}
.btn-outline-w{display:inline-block;margin-top:28px;border:2px solid #fff;border-radius:20px;padding:8px 20px;font-size:14px;color:#fff}
.arrow{top:278px;color:#fff;font-size:28px;font-weight:300}
.dots{left:588px;top:474px;display:flex;gap:8px}
.dots b{width:5px;height:5px;border-radius:50%;background:#fff;opacity:.5}
.dots b:first-child{opacity:1;background:#222}
.sec-title{width:1200px;text-align:center;font-size:28px;font-weight:400;color:var(--muted)}
.sec-title strong{color:var(--blue);font-weight:600}
.divider{left:465px;width:270px;height:20px}
.services{left:0;top:490px;width:1200px;height:574px;background:var(--grey-bg)}
.card{width:314px;height:366px;background:#fff;text-align:center;top:636px}
.card .ico{width:90px;height:90px;border-radius:50%;background:var(--blue);margin:26px auto 0;display:flex;align-items:center;justify-content:center}
.card h3{color:var(--blue);font-size:22px;font-weight:600;margin-top:24px}
.card p{font-size:14px;font-weight:300;line-height:23px;margin:14px 24px 0}
.card .price{font-size:18px;font-weight:600;color:#666;margin-top:30px}
.pill{display:inline-block;background:var(--grey-btn);color:#fff;border-radius:18px;font-size:13px;padding:8px 22px;margin-top:14px}
.pkg{background:#fafafa;box-shadow:0 2px 5px rgba(0,0,0,.12);text-align:center}
.pkg .head{background:var(--grey-head);color:#fff;font-size:22px;font-weight:600;display:flex;align-items:center;justify-content:center;height:97px}
.pkg.gold{background:#fff;z-index:2;overflow:hidden}
.pkg.gold .head{background:var(--blue)}
.amount{margin-top:30px;color:#444;display:flex;justify-content:center;align-items:flex-start;gap:2px}
.amount .cur{font-size:18px;margin-top:8px}
.amount .num{font-size:62px;font-weight:600;line-height:62px}
.amount .cents{font-size:18px;margin-top:4px}
.per{font-size:15px;margin-top:-4px;color:#444}
.list{margin:24px 42px 0;list-style:none}
.list li{height:44px;display:flex;align-items:center;justify-content:center;gap:10px;font-size:13px;color:#666;border-bottom:1px solid var(--line)}
.list li:last-child{border-bottom:0}
.sel{display:inline-block;margin-top:14px;border:1px solid #999;border-radius:22px;padding:10px 26px;font-size:15px;font-weight:300;color:#666}
.sel.solid{background:var(--blue);border-color:var(--blue);color:#fff}
.ribbon{right:-34px;top:26px;width:150px;transform:rotate(45deg);background:var(--green);color:#fff;font-size:10px;text-align:center;padding:4px 0;letter-spacing:.5px}
.why{left:0;top:1782px;width:1200px;height:650px;background:var(--grey-bg)}
.intro{top:1920px;width:1200px;text-align:center;font-size:15px;font-weight:300}
.feat{width:290px}
.feat h4{font-size:22px;font-weight:600;color:var(--blue);margin-top:8px}
.feat p{font-size:14px;font-weight:300;line-height:23px;margin-top:12px;color:#777}
.contact{left:0;top:2432px;width:1200px;height:558px;background:linear-gradient(180deg,#1c4a82,#1d4478)}
.contact h2{left:89px;top:2484px;font-size:28px;font-weight:600;color:#fff}
.contact h2 span{color:#4aa0e6}
.c-line{left:89px;top:2530px;width:190px;height:1px;background:#8aa6c8}
.c-lead{left:89px;top:2552px;font-size:14px;color:#fff;font-weight:300}
.field{background:#fff;border:1px solid #ccc;font-size:12px;color:#999;padding:0 10px;display:flex;align-items:center;height:34px}
.send{left:89px;top:2764px;width:230px;height:34px;border-radius:17px;background:#8a8a8a;color:#fff;font-size:13px;font-weight:700;display:flex;align-items:center;justify-content:center}
.info{color:#fff;font-size:14px;font-weight:300;line-height:23px}
.info b{font-weight:600;font-size:16px}
.person{left:846px;top:2406px;width:324px;height:584px;background:linear-gradient(180deg,#5d5a44,#4a5a3a 40%,#2f4a6d);border-radius:140px 140px 0 0}
.footer{left:0;top:2990px;width:1200px;height:102px;background:var(--footer);color:#fff;text-align:center}
.fnav{display:flex;justify-content:center;margin-top:22px;font-size:15px;font-weight:300}
.fnav span{padding:0 28px;border-right:1px solid #6d86a5}
.fnav span:last-child{border-right:0}
.copy{margin-top:16px;font-size:14px}
</style>
</head>
<body>

<div class="abs topbar">
  <span><svg width="13" height="13" viewBox="0 0 13 13"><rect x="1" y="3" width="11" height="8" fill="none" stroke="#cfe3f6" stroke-width="1.4"/><path d="M1 3l5.5 4L12 3" fill="none" stroke="#cfe3f6" stroke-width="1.4"/></svg>hello@ranklift.example</span>
  <span><svg width="13" height="13" viewBox="0 0 13 13"><path d="M3 1l2 3-1.5 1.5c.8 1.8 2.2 3.2 4 4L9 8l3 2-1 2C5 12 1 8 1 2z" fill="#cfe3f6"/></svg>+1-555-010-2040</span>
</div>

<header class="abs nav">
  <div class="brand"><i></i>RankLift</div>
  <nav class="menu">
    <span class="active">Home</span><span>About</span><span>Products</span><span>Contact</span>
    <svg width="22" height="18" viewBox="0 0 22 18"><path d="M1 2h3l2 9h10l2-7H6" fill="none" stroke="#1f6db5" stroke-width="2"/><circle cx="8" cy="15" r="1.6" fill="#1f6db5"/><circle cx="15" cy="15" r="1.6" fill="#1f6db5"/></svg>
  </nav>
</header>

<section class="abs hero" role="img" aria-label="Photo of a laptop showing a rising traffic chart in a meeting room, blue tinted"></section>
<div class="abs hero-copy">
  <h1>SEO Link Building</h1>
  <p>Lorem ipsum dolor sit amet consectetur adipiscing elit dolor</p>
  <span class="btn-outline-w">Learn More</span>
</div>
<div class="abs arrow" style="left:14px">&#8249;</div>
<div class="abs arrow" style="left:1172px">&#8250;</div>
<div class="abs dots"><b></b><b></b></div>

<section class="abs services"></section>
<h2 class="abs sec-title" style="top:542px">Our <strong>Services</strong></h2>
<svg class="abs divider" style="top:588px" viewBox="0 0 270 20"><line x1="0" y1="10" x2="120" y2="10" stroke="#ccc"/><line x1="150" y1="10" x2="270" y2="10" stroke="#ccc"/><rect x="128" y="5" width="9" height="6" rx="3" fill="none" stroke="#8fb6dc" stroke-width="2" transform="rotate(-40 132 8)"/><rect x="133" y="9" width="9" height="6" rx="3" fill="none" stroke="#8fb6dc" stroke-width="2" transform="rotate(-40 137 12)"/></svg>

<div class="abs card" style="left:110px">
  <div class="ico"><svg width="44" height="44" viewBox="0 0 44 44"><rect x="8" y="8" width="28" height="28" fill="none" stroke="#fff" stroke-width="2"/><line x1="13" y1="16" x2="31" y2="16" stroke="#fff" stroke-width="2"/><line x1="13" y1="23" x2="31" y2="23" stroke="#fff" stroke-width="2"/><line x1="13" y1="30" x2="24" y2="30" stroke="#fff" stroke-width="2"/></svg></div>
  <h3>Links</h3>
  <p>Lorem ipsum dolor sit amet, consectetur adipiscing elit</p>
  <div class="price">From £250</div>
  <span class="pill">See Products</span>
</div>
<div class="abs card" style="left:443px">
  <div class="ico"><svg width="44" height="44" viewBox="0 0 44 44"><rect x="10" y="7" width="24" height="30" fill="none" stroke="#fff" stroke-width="2"/><line x1="15" y1="15" x2="29" y2="15" stroke="#fff" stroke-width="2"/><line x1="15" y1="21" x2="29" y2="21" stroke="#fff" stroke-width="2"/><line x1="15" y1="27" x2="25" y2="27" stroke="#fff" stroke-width="2"/></svg></div>
  <h3>Content</h3>
  <p>Lorem ipsum dolor sit amet, consectetur adipiscing elit</p>
  <div class="price">From £150</div>
  <span class="pill">See Products</span>
</div>
<div class="abs card" style="left:775px">
  <div class="ico"><svg width="44" height="44" viewBox="0 0 44 44"><rect x="7" y="10" width="30" height="24" fill="none" stroke="#fff" stroke-width="2"/><line x1="7" y1="17" x2="37" y2="17" stroke="#fff" stroke-width="2"/><path d="M15 25l4 4 9-8" fill="none" stroke="#fff" stroke-width="2"/></svg></div>
  <h3>Monthly Packages</h3>
  <p>Lorem ipsum dolor sit amet, consectetur adipiscing elit</p>
  <div class="price">From £80</div>
  <span class="pill">See Products</span>
</div>

<h2 class="abs sec-title" style="top:1117px">Monthly <strong>Packages</strong></h2>
<svg class="abs divider" style="top:1164px" viewBox="0 0 270 20"><line x1="0" y1="10" x2="120" y2="10" stroke="#ccc"/><line x1="150" y1="10" x2="270" y2="10" stroke="#ccc"/><rect x="128" y="8" width="6" height="8" fill="#8fb6dc"/><rect x="136" y="8" width="6" height="8" fill="#8fb6dc"/></svg>

<div class="abs pkg" style="left:102px;top:1246px;width:331px;height:438px">
  <div class="head">Silver Package</div>
  <div class="amount"><span class="cur">£</span><span class="num">39</span><span class="cents">99</span></div>
  <div class="per">Monthly</div>
  <ul class="list">
    <li><svg width="16" height="16" viewBox="0 0 16 16"><circle cx="8" cy="8" r="7" fill="none" stroke="#666" stroke-width="1.3"/><path d="M4.5 8l2.5 2.5 4.5-5" fill="none" stroke="#666" stroke-width="1.4"/></svg>List Item #1</li>
    <li><svg width="16" height="16" viewBox="0 0 16 16"><circle cx="8" cy="8" r="7" fill="none" stroke="#666" stroke-width="1.3"/><path d="M4.5 8l2.5 2.5 4.5-5" fill="none" stroke="#666" stroke-width="1.4"/></svg>List Item #2</li>
    <li><svg width="16" height="16" viewBox="0 0 16 16"><circle cx="8" cy="8" r="7" fill="none" stroke="#666" stroke-width="1.3"/><path d="M4.5 8l2.5 2.5 4.5-5" fill="none" stroke="#666" stroke-width="1.4"/></svg>List Item #3</li>
  </ul>
  <span class="sel">Select Package</span>
</div>

<div class="abs pkg gold" style="left:433px;top:1219px;width:333px;height:492px">
  <div class="head">Gold Package</div>
  <div class="abs ribbon">POPULAR</div>
  <div class="amount"><span class="cur">£</span><span class="num">59</span><span class="cents">99</span></div>
  <div class="per">Monthly</div>
  <ul class="list">
    <li><svg width="16" height="16" viewBox="0 0 16 16"><circle cx="8" cy="8" r="7" fill="none" stroke="#666" stroke-width="1.3"/><path d="M4.5 8l2.5 2.5 4.5-5" fill="none" stroke="#666" stroke-width="1.4"/></svg>List Item #1</li>
    <li><svg width="16" height="16" viewBox="0 0 16 16"><circle cx="8" cy="8" r="7" fill="none" stroke="#666" stroke-width="1.3"/><path d="M4.5 8l2.5 2.5 4.5-5" fill="none" stroke="#666" stroke-width="1.4"/></svg>List Item #2</li>
    <li><svg width="16" height="16" viewBox="0 0 16 16"><circle cx="8" cy="8" r="7" fill="none" stroke="#666" stroke-width="1.3"/><path d="M4.5 8l2.5 2.5 4.5-5" fill="none" stroke="#666" stroke-width="1.4"/></svg>List Item #3</li>
    <li><svg width="16" height="16" viewBox="0 0 16 16"><circle cx="8" cy="8" r="7" fill="none" stroke="#666" stroke-width="1.3"/><path d="M4.5 8l2.5 2.5 4.5-5" fill="none" stroke="#666" stroke-width="1.4"/></svg>List Item #4</li>
  </ul>
  <span class="sel solid">Select Package</span>
</div>

<div class="abs pkg" style="left:766px;top:1246px;width:331px;height:438px">
  <div class="head">Platinum Package</div>
  <div class="amount"><span class="cur">£</span><span class="num">89</span><span class="cents">99</span></div>
  <div class="per">Monthly</div>
  <ul class="list">
    <li><svg width="16" height="16" viewBox="0 0 16 16"><circle cx="8" cy="8" r="7" fill="none" stroke="#666" stroke-width="1.3"/><path d="M4.5 8l2.5 2.5 4.5-5" fill="none" stroke="#666" stroke-width="1.4"/></svg>List Item #1</li>
    <li><svg width="16" height="16" viewBox="0 0 16 16"><circle cx="8" cy="8" r="7" fill="none" stroke="#666" stroke-width="1.3"/><path d="M4.5 8l2.5 2.5 4.5-5" fill="none" stroke="#666" stroke-width="1.4"/></svg>List Item #2</li>
    <li><svg width="16" height="16" viewBox="0 0 16 16"><circle cx="8" cy="8" r="7" fill="none" stroke="#666" stroke-width="1.3"/><path d="M4.5 8l2.5 2.5 4.5-5" fill="none" stroke="#666" stroke-width="1.4"/></svg>List Item #3</li>
  </ul>
  <span class="sel">Select Package</span>
</div>

<section class="abs why"></section>
<h2 class="abs sec-title" style="top:1835px">Why <strong>Choose</strong> Us</h2>
<svg class="abs divider" style="top:1881px" viewBox="0 0 270 20"><line x1="0" y1="10" x2="120" y2="10" stroke="#ccc"/><line x1="150" y1="10" x2="270" y2="10" stroke="#ccc"/><rect x="128" y="5" width="9" height="6" rx="3" fill="none" stroke="#8fb6dc" stroke-width="2" transform="rotate(-40 132 8)"/><rect x="133" y="9" width="9" height="6" rx="3" fill="none" stroke="#8fb6dc" stroke-width="2" transform="rotate(-40 137 12)"/></svg>
<p class="abs intro">Lorem ipsum dolor sit amet, consectetur adipiscing elit. Ut elit tellus, luctus nec ullamcorper mattis, pulvinar dapibus leo.</p>

<div class="abs feat" style="left:110px;top:1984px">
  <svg width="46" height="46" viewBox="0 0 46 46"><path d="M23 4l15 6v12c0 10-7 16-15 20C15 38 8 32 8 22V10z" fill="none" stroke="#888" stroke-width="2"/><path d="M16 23l5 5 9-10" fill="none" stroke="#888" stroke-width="2"/></svg>
  <h4>Trust</h4>
  <p>Lorem ipsum dolor sit amet, consectetur adipiscing elit. Ut elit tellus, luctus nec ullamcorper mattis, pulvinar dapibus leo.</p>
</div>
<div class="abs feat" style="left:443px;top:1984px">
  <svg width="46" height="46" viewBox="0 0 46 46"><rect x="6" y="4" width="28" height="38" fill="none" stroke="#888" stroke-width="2"/><line x1="11" y1="22" x2="29" y2="22" stroke="#888" stroke-width="2"/><line x1="11" y1="29" x2="29" y2="29" stroke="#888" stroke-width="2"/><circle cx="36" cy="12" r="6" fill="none" stroke="#888" stroke-width="2"/></svg>
  <h4>Experience</h4>
  <p>Lorem ipsum dolor sit amet, consectetur adipiscing elit. Ut elit tellus, luctus nec ullamcorper mattis, pulvinar dapibus leo.</p>
</div>
<div class="abs feat" style="left:775px;top:1984px">
  <svg width="46" height="46" viewBox="0 0 46 46"><rect x="4" y="4" width="38" height="14" fill="none" stroke="#888" stroke-width="2"/><circle cx="23" cy="27" r="5" fill="none" stroke="#888" stroke-width="2"/><path d="M13 44c0-6 4-10 10-10s10 4 10 10" fill="none" stroke="#888" stroke-width="2"/></svg>
  <h4>Customer Rates</h4>
  <p>Lorem ipsum dolor sit amet, consectetur adipiscing elit. Ut elit tellus, luctus nec ullamcorper mattis, pulvinar dapibus leo.</p>
</div>
<div class="abs feat" style="left:110px;top:2198px">
  <svg width="46" height="46" viewBox="0 0 46 46"><circle cx="24" cy="14" r="10" fill="none" stroke="#888" stroke-width="2"/><path d="M4 34l10-4h14l8-6 4 3-12 12H4" fill="none" stroke="#888" stroke-width="2"/></svg>
  <h4>Money Back Guarantee</h4>
  <p>Lorem ipsum dolor sit amet, consectetur adipiscing elit. Ut elit tellus, luctus nec ullamcorper mattis, pulvinar dapibus leo.</p>
</div>
<div class="abs feat" style="left:443px;top:2198px">
  <svg width="46" height="46" viewBox="0 0 46 46"><rect x="4" y="12" width="38" height="28" fill="none" stroke="#888" stroke-width="2"/><circle cx="28" cy="12" r="8" fill="none" stroke="#888" stroke-width="2"/><path d="M10 34l8-8 6 5 10-10" fill="none" stroke="#888" stroke-width="2"/></svg>
  <h4>Professional Expertise</h4>
  <p>Lorem ipsum dolor sit amet, consectetur adipiscing elit. Ut elit tellus, luctus nec ullamcorper mattis, pulvinar dapibus leo.</p>
</div>
<div class="abs feat" style="left:775px;top:2198px">
  <svg width="46" height="46" viewBox="0 0 46 46"><rect x="10" y="4" width="32" height="36" fill="none" stroke="#888" stroke-width="2"/><path d="M14 20l8 3v8c0 5-4 8-8 10-4-2-8-5-8-10v-8z" fill="#f2f4f6" stroke="#888" stroke-width="2"/><line x1="26" y1="14" x2="36" y2="14" stroke="#888" stroke-width="2"/></svg>
  <h4>Privacy &amp; Confidentiality</h4>
  <p>Lorem ipsum dolor sit amet, consectetur adipiscing elit. Ut elit tellus, luctus nec ullamcorper mattis, pulvinar dapibus leo.</p>
</div>

<section class="abs contact"></section>
<h2 class="abs contact" style="left:89px;top:2484px;width:auto;height:auto;background:none;font-size:28px;font-weight:600;color:#fff">Contact <span style="color:#4aa0e6">Me</span></h2>
<div class="abs c-line"></div>
<p class="abs c-lead">I want to talk to you. Get in touch with me today.</p>
<div class="abs field" style="left:89px;top:2584px;width:348px">Name</div>
<div class="abs field" style="left:446px;top:2584px;width:349px">Email</div>
<div class="abs field" style="left:89px;top:2629px;width:348px">Phone</div>
<div class="abs field" style="left:446px;top:2629px;width:349px">Subject</div>
<div class="abs field" style="left:89px;top:2673px;width:706px;height:81px;align-items:flex-start;padding-top:8px">Message</div>
<div class="abs send">SEND</div>

<svg class="abs" style="left:98px;top:2838px" width="16" height="20" viewBox="0 0 16 20"><path d="M8 1a6 6 0 0 1 6 6c0 5-6 12-6 12S2 12 2 7a6 6 0 0 1 6-6z" fill="#4aa0e6"/><circle cx="8" cy="7" r="2.3" fill="#1c4a82"/></svg>
<p class="abs info" style="left:129px;top:2836px;width:330px">Lorem ipsum dolor sit amet, consectetur adipiscing elit. Ut elit tellus, luctus nec ullamcorper mattis, pulvinar dapibus leo.</p>
<svg class="abs" style="left:473px;top:2842px" width="18" height="18" viewBox="0 0 13 13"><path d="M3 1l2 3-1.5 1.5c.8 1.8 2.2 3.2 4 4L9 8l3 2-1 2C5 12 1 8 1 2z" fill="#4aa0e6"/></svg>
<p class="abs info" style="left:504px;top:2838px"><b>05550102233</b></p>
<svg class="abs" style="left:473px;top:2886px" width="18" height="16" viewBox="0 0 13 13"><rect x="1" y="3" width="11" height="8" fill="none" stroke="#4aa0e6" stroke-width="1.6"/><path d="M1 3l5.5 4L12 3" fill="none" stroke="#4aa0e6" stroke-width="1.6"/></svg>
<p class="abs info" style="left:504px;top:2882px"><b>hello@ranklift.example</b></p>

<div class="abs person" role="img" aria-label="Photo of the agency founder standing and gesturing, olive t-shirt and jeans"></div>

<footer class="abs footer">
  <div class="fnav"><span>Home</span><span>About</span><span>Products</span><span>Contact</span></div>
  <div class="copy">© 2020 RankLift All Rights Reserved.</div>
</footer>

</body>
</html>
```